Bref créative
Home provement Flyer/Door hanger
Kitchen,bathroom,windows
Im looking to make flyer or door hanger for home improvement company. I was thinking front side with kitchen & bathroom.
Back side windows.
Construction
Professional, corporate,
Tallow Ridge Builders, LLC
4817 Copper Fern RD
Suite 812
Vienna, VA 22182
Tel: 571 238 6054
www.tallowridgebuilders.example
We offer Financing
Free Estimate
I need the design to be on AI, EPS AND PSD FILE. I need them by each layer so i can edit later if i need to.
This is the company logo.
You may visit www.tallowridgebuilders.example and choose a right picture from the gallery

```html
<!DOCTYPE html>
<html lang="en">
<head>
<meta charset="utf-8">
<title>Tallow Ridge Builders – Flyer and Door Hangers</title>
<link href="https://fonts.googleapis.com/css2?family=Oswald:wght@400;600&family=Open+Sans:wght@400;600;700&display=swap" rel="stylesheet">
<style>
  :root{
    --canvas:#e4e2df;
    --paper:#ffffff;
    --fold:#e8e9eb;
    --fold-shade:#d3d5d8;
    --green:#7cbf2a;
    --green-dark:#5d9a17;
    --ink:#3b3d40;
    --ink-soft:#7a7d82;
    --footer:#2d2f33;
    --badge:#1f2023;
    --kitchen:#f07f1b;
    --bathroom:#7a2f8f;
    --additions:#5ea61e;
    --exteriors:#d9312b;
  }
  *{box-sizing:border-box;margin:0;padding:0}
  html,body{width:1200px;height:850px;overflow:hidden;background:var(--canvas)}
  body{position:relative;font-family:"Open Sans",sans-serif;color:var(--ink)}

  /* ---------- Flyer ---------- */
  .flyer{position:absolute;left:60px;top:60px;width:520px;height:730px;background:var(--paper);box-shadow:0 8px 24px rgba(0,0,0,.18);overflow:hidden}
  .flyer-header{position:absolute;left:0;top:0;width:520px;height:260px}
  .flyer-header svg{position:absolute;inset:0}
  .brand{position:absolute;display:flex;align-items:center;gap:8px;font-family:"Oswald",sans-serif;font-weight:600;color:var(--ink);text-transform:uppercase;letter-spacing:.5px;white-space:nowrap}
  .brand-mark{width:18px;height:18px;background:var(--green)}
  .flyer .brand{left:150px;top:64px;font-size:21px}
  .best-badge{position:absolute;border-radius:50%;background:var(--badge);border:4px solid #c9cbce}
  .flyer .best-badge{left:26px;top:150px;width:76px;height:76px}
  .call-block{position:absolute;font-family:"Oswald",sans-serif;color:#fff;transform-origin:left top;text-transform:uppercase;line-height:1.05;white-space:nowrap}
  .flyer .call-block{left:336px;top:176px;transform:rotate(-32deg);font-size:26px;font-weight:600}
  .call-block .phone{display:flex;align-items:center;gap:6px;font-size:.9em;font-weight:400}
  .photo{position:absolute}
  .flyer .photo{left:0;top:260px;width:520px;height:270px;background:linear-gradient(160deg,#cfd2d4 0%,#8d8f93 35%,#3a3b3e 65%,#b98a56 100%)}
  .services{position:absolute;left:44px;top:548px;display:grid;grid-template-columns:1fr 1fr;gap:10px 28px;width:432px}
  .service{font-family:"Oswald",sans-serif;color:#fff;text-transform:uppercase;font-size:19px;line-height:24px;text-align:center;padding:6px 0;letter-spacing:1px}
  .service.kitchen{background:var(--kitchen)}
  .service.bathroom{background:var(--bathroom)}
  .service.additions{background:var(--additions)}
  .service.exteriors{background:var(--exteriors)}
  .flyer-footer{position:absolute;left:0;bottom:0;width:520px;height:72px;background:var(--footer);color:#e6e7e8;padding:12px 30px;font-size:13px;line-height:1.5}
  .flyer-footer .tel{font-weight:700;color:#fff}
  .flyer-footer .web{color:var(--green)}

  /* ---------- Door hangers ---------- */
  .hanger{position:absolute;top:105px;width:210px;height:640px;background:var(--paper);border-radius:60px 60px 0 0;box-shadow:0 8px 24px rgba(0,0,0,.18);overflow:hidden}
  .hanger-hole{position:absolute;left:60px;top:28px;width:90px;height:90px;border-radius:50%;background:var(--canvas)}
  .hanger-slit{position:absolute;left:100px;top:110px;width:10px;height:40px;background:var(--canvas)}
  .hanger .brand{left:0;right:0;justify-content:center;top:170px;font-size:15px}
  .hanger-front{left:650px}
  .hanger-front svg{position:absolute;left:0;top:0}
  .hanger-front .call-block{left:22px;top:424px;transform:rotate(-33.7deg);font-size:21px;font-weight:600}
  .hanger-front .call-block .phone{font-size:.88em}
  .hanger-front .photo{left:0;top:380px;width:210px;height:260px;background:linear-gradient(150deg,#f1e6d4 0%,#c28a4e 45%,#6b4a2b 100%);clip-path:polygon(0 53.8%,100% 0,100% 100%,0 100%)}
  .hanger-back{left:920px}
  .hanger-back .best-badge{left:62px;top:220px;width:86px;height:86px}
  .hanger-back .details{position:absolute;left:0;right:0;top:470px;text-align:center;font-size:11px;line-height:1.6;color:var(--ink)}
  .hanger-back .details .tel{font-weight:700}
  .hanger-back .details .web{color:var(--green-dark)}
  .hanger-back .base{position:absolute;left:0;bottom:0;width:210px;height:34px;background:var(--green)}
</style>
</head>
<body>

<section class="flyer">
  <div class="flyer-header">
    <svg width="520" height="260" viewBox="0 0 520 260" aria-hidden="true">
      <rect width="520" height="260" fill="var(--fold)"/>
      <polygon points="0,0 520,0 520,40 255,210 0,70" fill="var(--paper)"/>
      <polygon points="0,70 255,210 255,218 0,80" fill="var(--fold-shade)"/>
      <polygon points="300,180 520,40 520,170 380,260 300,260" fill="var(--green)"/>
      <polygon points="300,180 520,40 520,52 308,188" fill="var(--green-dark)"/>
    </svg>
    <div class="brand"><span class="brand-mark"></span>Tallow Ridge Builders</div>
    <div class="best-badge" aria-hidden="true"></div>
    <div class="call-block">
      Call us now
      <div class="phone">
        <svg width="16" height="16" viewBox="0 0 24 24" aria-hidden="true"><path fill="#fff" d="M6.6 10.8a15.1 15.1 0 0 0 6.6 6.6l2.2-2.2c.3-.3.7-.4 1-.2 1.1.4 2.3.6 3.6.6.6 0 1 .4 1 1V20c0 .6-.4 1-1 1A17 17 0 0 1 3 4c0-.6.4-1 1-1h3.5c.6 0 1 .4 1 1 0 1.3.2 2.5.6 3.6.1.3 0 .7-.2 1z"/></svg>
        571 238 6054
      </div>
    </div>
  </div>
  <div class="photo" role="img" aria-label="Photo of a remodeled modern kitchen with dark cabinets and a large island"></div>
  <div class="services">
    <div class="service kitchen">Kitchen</div>
    <div class="service bathroom">Bathroom</div>
    <div class="service additions">Additions</div>
    <div class="service exteriors">Exteriors</div>
  </div>
  <footer class="flyer-footer">
    4817 Copper Fern RD, Suite 812, Vienna, VA 22182<br>
    <span class="tel">Tel.: 571 238 6054</span> &nbsp; <span class="web">www.tallowridgebuilders.example</span>
  </footer>
</section>

<section class="hanger hanger-front">
  <svg width="210" height="640" viewBox="0 0 210 640" aria-hidden="true">
    <polygon points="0,420 210,280 210,380 0,520" fill="var(--green)"/>
  </svg>
  <div class="hanger-hole"></div>
  <div class="hanger-slit"></div>
  <div class="brand"><span class="brand-mark"></span>Tallow Ridge</div>
  <div class="call-block">
    Call us now
    <div class="phone">571 238 6054</div>
  </div>
  <div class="photo" role="img" aria-label="Photo of a bright kitchen interior with wood cabinets"></div>
</section>

<section class="hanger hanger-back">
  <div class="hanger-hole"></div>
  <div class="hanger-slit"></div>
  <div class="brand"><span class="brand-mark"></span>Tallow Ridge</div>
  <div class="best-badge" aria-hidden="true"></div>
  <div class="details">
    4817 Copper Fern RD, Suite 812<br>
    Vienna, VA 22182<br>
    <span class="tel">Tel.: 571 238 6054</span><br>
    <span class="web">www.tallowridgebuilders.example</span>
  </div>
  <div class="base"></div>
</section>

</body>
</html>
```